Flyer für Freie Referentin
I thank Merak Tuwero for the great work! I’am very satisfied with the design of my flyer, with the arrangement of the photos, the font and the colors. Everything is fine and exactly as I imagined before. All my requested changings were changed very quickly and correctly. I would definitely recommend this designer!
Zielgruppe
Ich biete Vorträge, Kurse, Fortbildungen und Privatunterricht an zu den Themen:
Einführung in die Weltreligionen
und
Feste der Religionen
Außerdem biete ich Führungen durch religiöse Gebäude in Berlin an.
Meine Zielgruppen sind:
1. Pädagogen in Kita, Grund-und Oberschule,
2. Religionslehrer,
3.Fachkräfte im interkulturellen Kontext (Ausländerbehörde, Gesundheitswesen, Sozialwesen) und
4. Menschen, die gern reisen und sich für andere Religionen und Kulturen interessieren
Aufgabenstellung
Ich habe selbst einen 6 seitigen Falzflyer entworfen, mit Text und Bildern und würde diesen inhaltlich weitgehend so lassen, und nur in einem ansprechenden Design umgestalten lassen. Die Fotos, die ich liefere, habe ich in den religiösen Gebäuden selbst gemacht.

```html
<!DOCTYPE html>
<html lang="de">
<head>
<meta charset="utf-8">
<title>Weltreligionen in Berlin erleben – Faltflyer</title>
<link rel="stylesheet" href="https://fonts.googleapis.com/css2?family=Open+Sans:wght@300;400;600;700;800&display=swap">
<style>
:root{
  --bg:#dcdcdc;
  --yellow:#f5bd45;
  --olive:#6a7a28;
  --khaki:#c4b062;
  --pale:#f6ebb8;
  --cream:#fdfbee;
  --rust:#d1501c;
  --maroon:#8f1c24;
  --lime:#a6c62a;
  --moss:#5e6e2c;
  --ink:#1e1e1e;
  --white:#ffffff;
}
*{box-sizing:border-box;margin:0;padding:0}
html,body{width:1200px;height:1092px;overflow:hidden;background:var(--bg);font-family:"Open Sans",Arial,sans-serif}
.spread{position:absolute;left:12px;width:1176px;height:526px;display:flex;box-shadow:0 4px 12px rgba(0,0,0,.25)}
.spread--inside{top:12px}
.spread--outside{top:554px}
.panel{position:relative;width:392px;height:100%;padding:22px 22px;overflow:hidden}
.panel--yellow{background:var(--yellow)}
.panel--olive{background:var(--olive);color:var(--pale)}
.panel--pale{background:var(--pale);color:var(--ink)}
.panel--cream{background:var(--cream)}
.panel--khaki{background:var(--khaki);color:var(--white)}
.photo{display:block;border-radius:1px}
h2{font-weight:400;font-size:16px;line-height:1.25}
.h-maroon{color:var(--maroon)}
ul.bullets{list-style:none;font-size:10.5px;line-height:1.9}
ul.bullets li::before{content:"• "}

/* inside: offer */
.offer .photo{height:270px;background:linear-gradient(160deg,#c8d4e4 0%,#d6a06a 35%,#2f8c86 60%,#c8766a 100%)}
.offer h2{margin-top:18px}
.offer .lead{font-size:14px;color:var(--maroon);margin-top:6px}
.offer ul{color:var(--maroon);margin-top:8px}
.offer ul li{line-height:1.7;margin-bottom:3px}

/* inside: visits */
.visits h2{font-size:15px}
.visits ul{margin-top:6px;font-size:9.5px;line-height:1.9}
.visits .photo{height:268px;margin-top:10px;background:linear-gradient(170deg,#8aa86a 0%,#b9b2a4 40%,#c66a32 65%,#6b4a3a 100%)}
.visits h2.take{margin-top:22px}
.visits .take-list{font-size:9.5px;margin-top:4px}

/* inside: audience */
.audience h2{font-size:14px;font-weight:600}
.audience ol{list-style:none;margin-top:6px}
.audience ol>li{font-size:11px;font-weight:600;margin-top:7px}
.audience ol>li small{display:block;font-size:8px;font-weight:400}
.audience ol>li p{font-size:9px;font-weight:400;padding-left:10px;margin-top:2px;line-height:1.45}
.audience .pair{display:flex;gap:6px;margin-top:12px}
.audience .pair .photo{flex:1;height:194px}
.ph-procession{background:linear-gradient(170deg,#7aa25a 0%,#e8e4dc 45%,#c7a25a 100%)}
.ph-monks{background:linear-gradient(170deg,#9fbf7a 0%,#e89a2a 50%,#c86818 100%)}

/* outside: about */
.about h2{font-size:14px}
.about .photo{width:300px;height:230px;margin:8px 0 0 10px;background:radial-gradient(circle at 50% 40%,#f2b36a 0%,#f0a032 70%)}
.badge{position:absolute;border-radius:50%;color:var(--white);font-size:9px;line-height:1.25;text-align:center;display:flex;align-items:center;justify-content:center;padding:8px}
.badge--diss{background:var(--rust);left:38px;top:290px;width:84px;height:84px}
.badge--study{background:var(--lime);left:255px;top:268px;width:84px;height:84px}
.badge--ref{background:var(--maroon);left:192px;top:338px;width:92px;height:92px}
.badge--author{background:var(--moss);left:22px;top:378px;width:92px;height:92px}

/* outside: contact */
.contact{padding-right:90px}
.contact .strip{position:absolute;right:0;top:0;width:74px;height:100%;background:var(--olive)}
.contact h2{font-size:13px;font-weight:600}
.contact .name{font-size:11px;margin-top:10px}
.contact .role{font-size:8px;opacity:.9}
.contact dl{display:grid;grid-template-columns:32px 1fr;font-size:9px;line-height:1.35;margin-top:6px}
.contact .photo{position:relative;width:220px;height:150px;margin-top:14px;background:linear-gradient(150deg,#2e7a3a 0%,#e0a040 45%,#8a4a2a 60%,#3a8a3a 100%);z-index:1}
.contact h3{font-size:12px;font-weight:600;margin-top:14px}
.contact .text{font-size:8.5px;line-height:1.4;margin-top:8px}

/* cover */
.cover{padding:0}
.cover .top{height:10px;background:#f8f2d6}
.cover .symbols{width:300px;height:210px;margin:30px auto 0;border-radius:2px;background:radial-gradient(circle at 50% 50%,#d8d4c6 0%,#ece8d8 60%,#f7f4e6 100%)}
.cover .title{background:var(--rust);color:var(--white);font-weight:800;font-size:26px;line-height:1.22;padding:12px 20px;margin-top:14px}
.cover .sub{color:var(--rust);font-weight:300;font-size:20px;line-height:1.25;padding:14px 20px 0}
.cover .url{position:absolute;right:28px;bottom:18px;font-size:9px;color:var(--rust)}
</style>
</head>
<body>

<section class="spread spread--inside">
  <div class="panel panel--yellow offer">
    <div class="photo" role="img" aria-label="Foto: Frauen in bunten Gewändern bei einem Fest in einer Moschee"></div>
    <h2 class="h-maroon">Weltreligionen verstehen –<br>Menschen besser begegnen</h2>
    <p class="lead">Mein Angebot:</p>
    <ul class="bullets">
      <li>Vorträge &amp; Seminare zu: Judentum, Christentum, Islam, Hinduismus und Buddhismus</li>
      <li>Vorträge &amp; Seminare zu religiösen Festen und Traditionen</li>
      <li>Besuche religiöser Stätten</li>
      <li>Individuelle Weiterbildungen &amp; Privatunterricht</li>
    </ul>
  </div>
  <div class="panel panel--olive visits">
    <h2>Besuche religiöser Stätten</h2>
    <ul class="bullets">
      <li>Führung durch die Räume</li>
      <li>Teilnahme an Zeremonien</li>
      <li>Austausch mit Gläubigen</li>
    </ul>
    <div class="photo" role="img" aria-label="Foto: Tänzer bei einer hinduistischen Straßenprozession"></div>
    <h2 class="take">Was Sie mitnehmen:</h2>
    <ul class="bullets take-list">
      <li>Klar verständliches Wissen zu den Weltreligionen</li>
      <li>Hintergründe zu Festen, Bräuchen und Symbolen</li>
      <li>Aha-Momente für Beruf, Alltag und Reisen</li>
    </ul>
  </div>
  <div class="panel panel--pale audience">
    <h2>Meine Angebote richten sich an:</h2>
    <ol>
      <li>1. Lehrkräfte allgemein:
        <p>• Gewinnen Sie fundiertes Wissen, um Schüler*innen unterschiedlicher Herkunft besser zu begleiten</p></li>
      <li>2. Religionslehrerinnen und Religionslehrer:
        <p>• Vertiefen Sie Ihr Wissen zu Inhalten der großen Religionen – praxisnah und aktuell!</p></li>
      <li>3. Fachkräfte im interkulturellen Kontext:
        <small>(Ausländerbehörde, Asylberatung, Gesundheitswesen)</small>
        <p>• Gewinnen Sie Sicherheit im Umgang mit religiös geprägten Verhaltensweisen!</p></li>
      <li>4. Reisefreudige &amp; Neugierige:
        <p>• Entdecken Sie spannende Einblicke in Rituale, Werte und Feiertage weltweit!</p></li>
    </ol>
    <div class="pair">
      <div class="photo ph-procession" role="img" aria-label="Foto: äthiopisch-orthodoxe Prozession im Freien"></div>
      <div class="photo ph-monks" role="img" aria-label="Foto: buddhistische Mönche in orangefarbenen Roben"></div>
    </div>
  </div>
</section>

<section class="spread spread--outside">
  <div class="panel panel--yellow about">
    <h2 class="h-maroon">Über mich</h2>
    <div class="photo" role="img" aria-label="Porträtfoto der Referentin vor orangem Hintergrund"></div>
    <div class="badge badge--diss">2008<br>Dissertation:<br>„Hindus in der deutschen Diaspora.“</div>
    <div class="badge badge--study">1992-1999<br>Studium der Religionswis&shy;senschaft und Indologie in Berlin</div>
    <div class="badge badge--ref">Seit 2000<br>Wissenschaftliche Referentin für Weltreligionen und Hinduismus</div>
    <div class="badge badge--author">Seit 2002<br>Freie Autorin, Schwerpunkt: Religiöse Gruppen in der Diaspora</div>
  </div>
  <div class="panel panel--khaki contact">
    <div class="strip"></div>
    <h2>Kontakt</h2>
    <p class="name">Dr. Helke Marrau</p>
    <p class="role">Religionswissenschaftlerin und Indologin</p>
    <dl>
      <dt>Büro:</dt><dd>Lindenhofweg 7<br>10115 Berlin</dd>
      <dt>Tel.:</dt><dd>030 55501234</dd>
      <dt>Mobil:</dt><dd>017655509876</dd>
      <dt>Mail:</dt><dd>info@fermoxabbe.de</dd>
      <dt>Web:</dt><dd>www.fermoxabbe.de</dd>
    </dl>
    <div class="photo" role="img" aria-label="Foto: Hände halten eine Schale mit Opferfeuer"></div>
    <h3>Mehr Infos &amp; Buchung</h3>
    <p class="text">Ich biete Seminare für Einzelpersonen, Bildungseinrichtungen und Teams an – in meinem Büro oder vor Ort.</p>
    <p class="text">• Aktuelle Preise und Konditionen finden Sie auf meiner Website. www.fermoxabbe.de</p>
    <p class="text">• Individuelle Angebote – Preise auf Nachfrage unter: info@fermoxabbe.de<br>oder: Tel.: 03(0) 55501 234</p>
  </div>
  <div class="panel panel--cream cover">
    <div class="top"></div>
    <div class="symbols" role="img" aria-label="Illustration: Gruppe von Symbolen der fünf Weltreligionen"></div>
    <h1 class="title">Weltreligionen<br>in Berlin erleben</h1>
    <p class="sub">Vorträge &amp; Seminare<br>Führungen &amp; Privat-<br>unterricht in Berlin</p>
    <p class="url">www.fermoxabbe.de</p>
  </div>
</section>

</body>
</html>
```